Templates for Construction Company

We are looking to have templates prepared for all aspects of our letter sending. Using our brand design. with similar layouts that look the same.

Letterheads design & Email signatures

We use letter heads for - quotes, contract correspondence, variations, formal letters, invitations

Target Market(s)

Clients documents sent in emails

Industry/Entity Type

Construction

Font styles to use
Serif
Sans Serif

Colors
0054AA
0677BA
7BADD7
CADEEF
E8F1F8

Requirements
Must have
• Easy to read, water marks on page
Nice to have
• Different options for different letters

```html
<!DOCTYPE html>
<html lang="en">
<head>
<meta charset="utf-8">
<title>Ridgeline Builders Letterhead</title>
<link href="https://fonts.googleapis.com/css2?family=Didact+Gothic&display=swap" rel="stylesheet">
<style>
  :root {
    --backdrop: #9c9c9c;
    --paper-light: #ffffff;
    --paper-shade: #e5e5e5;
    --brand-blue: #4f85c8;
    --band-grey: #5f5f5f;
    --ink: #3a3a3a;
    --ink-soft: #666666;
    --watermark: #e9eef5;
  }
  * { margin: 0; padding: 0; box-sizing: border-box; }
  html, body { width: 1200px; height: 887px; overflow: hidden; }
  body {
    background: var(--backdrop);
    font-family: "Didact Gothic", "Century Gothic", sans-serif;
    color: var(--ink);
    position: relative;
  }
  .sheet {
    position: absolute;
    top: 78px;
    width: 522px;
    height: 730px;
    background: linear-gradient(100deg, var(--paper-light) 35%, var(--paper-shade) 100%);
    box-shadow: 0 6px 18px rgba(0,0,0,0.25);
    overflow: hidden;
  }
  .sheet--letter { left: 60px; }
  .sheet--follow { left: 630px; }

  .watermark {
    position: absolute;
    width: 240px;
    font-size: 40px;
    line-height: 46px;
    color: var(--watermark);
    text-align: center;
    z-index: 0;
    user-select: none;
  }
  .sheet--letter .watermark { left: 112px; top: 336px; }
  .sheet--follow .watermark { left: 140px; top: 326px; }

  .brand {
    position: absolute;
    left: 47px;
    top: 66px;
    display: flex;
    align-items: flex-start;
    gap: 6px;
    z-index: 1;
  }
  .brand-mark {
    width: 12px;
    height: 12px;
    margin-top: 6px;
    background: var(--brand-blue);
  }
  .brand-name {
    font-size: 22px;
    line-height: 24px;
    color: var(--brand-blue);
  }

  .contact {
    position: absolute;
    left: 184px;
    top: 86px;
    font-size: 10.5px;
    color: var(--ink);
    z-index: 1;
  }
  .contact-address {
    padding-bottom: 2px;
    border-bottom: 1.5px solid var(--brand-blue);
    width: 288px;
    white-space: nowrap;
  }
  .contact-lines {
    margin-top: 5px;
    white-space: nowrap;
  }

  .letter {
    position: absolute;
    left: 47px;
    top: 204px;
    width: 431px;
    z-index: 1;
  }
  .salutation {
    font-size: 13.5px;
    margin-bottom: 23px;
  }
  .letter p {
    font-size: 8px;
    line-height: 11.2px;
    color: var(--ink-soft);
    text-align: justify;
    margin-bottom: 11.2px;
  }
  .closing {
    margin-top: 22px;
    font-size: 8px;
    color: var(--ink-soft);
  }
  .signature {
    display: block;
    margin-top: 20px;
    width: 60px;
    height: 18px;
    background: linear-gradient(90deg, #d9dde3, #eef0f3);
  }

  .footer-band {
    position: absolute;
    left: 0;
    bottom: 0;
    width: 100%;
    height: 7px;
  }
</style>
</head>
<body>

<section class="sheet sheet--letter">
  <div class="watermark" aria-hidden="true">Ridgeline<br>Builders</div>

  <div class="brand">
    <span class="brand-mark"></span>
    <span class="brand-name">Ridgeline<br>Builders</span>
  </div>

  <div class="contact">
    <div class="contact-address">4120 Cedar Hollow Road, Juneau, Alaska 99801</div>
    <div class="contact-lines">555-214-7730| name@ridgelinebuilders.com &nbsp;|&nbsp; ridgelinebuilders.com</div>
  </div>

  <div class="letter">
    <div class="salutation">Dear Mr. Harlan,</div>
    <p>Lorem ipsum dolor sit amet, consectetur adipiscing elit. Donec orci purus, luctus vitae dignissim eu, iaculis sed purus. Vivamus faucibus, ipsum nec aliquet viverra, leo mauris condimentum ligula, sit amet sagittis enim ligula quis arcu. Nam egestas tortor id nisi porttitor mattis. In tortor ante, ultricies in suscipit a, tempus non massa. Vivamus et auctor mi. Fusce vel massa nulla. Phasellus nec eros mauris, et scelerisque orci.</p>
    <p>Donec malesuada orci vitae nulla accumsan porta a id massa. Quisque accumsan iaculis magna sit amet fringilla. Maecenas consequat, magna eget tincidunt semper, odio nibh rutrum mi, id feugiat ante nisi eu risus. Vestibulum nunc orci, rhoncus a placerat in, ultricies in mi. Cras mattis varius eros, vel fringilla nisi suscipit eget. Quisque scelerisque sagittis nulla at porttitor.</p>
    <p>Sed id augue vitae urna euismod commodo aliquet a quam. Pellentesque arcu velit, cursus et malesuada ut, consequat et diam. Nullam erat sem, rhoncus id ullamcorper vitae, rhoncus et arcu. In ultricies ultricies nulla, ut rutrum nisi iaculis at. Donec eu magna a metus ornare faucibus. Fusce aliquet faucibus ultricies. Morbi semper, est id tincidunt gravida, sem arcu adipiscing lacus, ac bibendum nulla leo eu purus. Quisque nec diam sed risus consectetur accumsan quis quis nibh. Vestibulum id purus lorem.</p>
    <p>It is a long established fact that a reader will be distracted by the readable content of a page when looking at its layout. The point of using Lorem Ipsum is that it has a more-or-less normal distribution of letters, as opposed to using 'Content here, content here', making it look like readable English. Many desktop publishing packages</p>
    <div class="closing">Sincerely,</div>
    <span class="signature" role="img" aria-label="Handwritten signature"></span>
  </div>

  <svg class="footer-band" viewBox="0 0 522 7" preserveAspectRatio="none">
    <polygon points="0,0 413,0 420,7 0,7" fill="var(--brand-blue)"/>
    <polygon points="417,0 522,0 522,7 424,7" fill="var(--band-grey)"/>
  </svg>
</section>

<section class="sheet sheet--follow">
  <div class="watermark" aria-hidden="true">Ridgeline<br>Builders</div>

  <svg class="footer-band" viewBox="0 0 522 7" preserveAspectRatio="none">
    <polygon points="0,0 410,0 417,7 0,7" fill="var(--brand-blue)"/>
    <polygon points="414,0 522,0 522,7 421,7" fill="var(--band-grey)"/>
  </svg>
</section>

</body>
</html>
```